Business Card for Professional Domainer

Require a business card design for an Individual Person who is a Professional Domainer.

Who is a Professional Domainer?
A domainer is someone who earns a profit buying and selling domain names.
Professional Domainer are the ones who do this on a full time basis.

So we require the business card design to be related to the above work.

There is no company or any logo currently, as the card is required for an Individual Person.

Business Card required to mention following details:

1. Full Name of the Person (Ex: Marisol Kettner)
2. Education Qualification (Ex: B.Tech Computer Science)
3. Mobile Number (Ex: +71 4837160295)
4. Website (Ex: www.trelmixo.com)
5. Email (Ex: hello@trelmixo.com)

Positioning of the details:

1. Mobile Number should be placed to Right Top Corner
2. Education Qualification should be just below Full Name
3. Website and Email should be on Bottom Part, on a bar at the bottom

It's important to include images related to the nature of work (Domaining) in the card design.
A good related image would be great. Image should be either in background or as a logo.
The image should be focus of the business card, and shoudl speak out on itself.
Anyone looking at the card should understand at one look what work is being done.
So kindly use images in the design which are highly relevant to domaining and domain names.

Along with the image, it's also good if you use the word "Professional Domainer" anywhere in the design.
Maybe along with the image or somewhere it would fit. These words would be like company name.
So please try to use these words "Professional Domainer" in the design, as it will help a lot.

Colors: Blue, Red, Green

We like these colors, but you are free to use any color which would be good for the design.

Card design should be according to Quornalex specs:

Document Trim Size = 91 x 55 mm | 1075 x 650 pixels
Full Bleed Size = 94 x 58 mm | 1110 x 685 pixels

Last thing, the business card should look professional and clean.
People should know that the person is a Professional Domainer at one look of the card.

Thank You and All the Best :)

Message to the the designers working on this project:

We have now guaranteed this project. This means, we will 100% choose a design and award the project to the one we like the best. So kindly submit your best designs before Wednesday, 3 July 2013. After that we are going to finalize the project and award to the best one. So please hurry up so that you are not too late. Thank You and All the Best!

```html
<!DOCTYPE html>
<html lang="en">
<head>
<meta charset="utf-8">
<title>Marisol Kettner – Professional Domainer business card</title>
<link rel="stylesheet" href="https://fonts.googleapis.com/css2?family=Questrial&family=Montserrat:wght@700&family=Roboto:wght@700&display=swap">
<style>
  :root {
    --page-bg: #e9ecee;
    --teal-deep: #163f4d;
    --teal-mid: #2f6f83;
    --teal-glow: #7fc2d4;
    --shirt-light: #d9dde0;
    --jacket-dark: #1b1d22;
    --bar-blue: #5d93ad;
    --bar-ink: #17232d;
    --frame-line: #6aa3ba;
    --title-ink: #f2f4f5;
  }
  * { margin: 0; padding: 0; box-sizing: border-box; }
  html, body {
    width: 1200px;
    height: 871px;
    overflow: hidden;
    background: var(--page-bg);
  }
  .card {
    position: absolute;
    left: 100px;
    top: 133px;
    width: 1000px;
    height: 605px;
    overflow: hidden;
    box-shadow: 0 6px 22px rgba(0,0,0,0.18);
  }
  .card__photo {
    position: absolute;
    inset: 0;
    background:
      radial-gradient(ellipse 55% 60% at 62% 40%, var(--teal-glow) 0%, var(--teal-mid) 45%, transparent 80%),
      linear-gradient(90deg, var(--shirt-light) 0%, var(--shirt-light) 12%, var(--jacket-dark) 26%, var(--jacket-dark) 34%, var(--teal-mid) 52%, var(--teal-deep) 100%);
  }
  .contact-bar {
    position: absolute;
    left: 72px;
    top: 0;
    width: 128px;
    height: 605px;
    background: var(--bar-blue);
  }
  .contact-bar__lines {
    position: absolute;
    left: 50%;
    top: 50%;
    width: 560px;
    transform: translate(-50%, -50%) rotate(-90deg);
    display: flex;
    flex-direction: column;
    gap: 4px;
    font-family: "Roboto", Arial, sans-serif;
    font-weight: 700;
    color: var(--bar-ink);
  }
  .contact-bar__web,
  .contact-bar__email { font-size: 24px; line-height: 1.15; }
  .contact-bar__phone { font-size: 36px; line-height: 1.15; margin-top: 4px; }
  .title-frame {
    position: absolute;
    left: 338px;
    top: 58px;
    width: 560px;
    height: 300px;
    border: 7px solid var(--frame-line);
  }
  .brand-title {
    position: absolute;
    left: 362px;
    top: 76px;
    font-family: "Questrial", "Century Gothic", sans-serif;
    font-size: 60px;
    line-height: 1.08;
    color: var(--title-ink);
    letter-spacing: 1px;
  }
  .person {
    position: absolute;
    left: 352px;
    top: 378px;
    color: var(--title-ink);
  }
  .person__name {
    font-family: "Montserrat", "Century Gothic", sans-serif;
    font-weight: 700;
    font-size: 58px;
    line-height: 1.05;
    letter-spacing: 1px;
  }
  .person__degree {
    font-family: "Questrial", "Century Gothic", sans-serif;
    font-size: 30px;
    line-height: 1.2;
    letter-spacing: 1px;
  }
</style>
</head>
<body>
  <div class="card">
    <div class="card__photo" role="img" aria-label="Photo of a business person in a dark jacket touching a glowing network of connected points on a teal screen"></div>

    <div class="contact-bar">
      <div class="contact-bar__lines">
        <span class="contact-bar__web">www.trelmixo.com</span>
        <span class="contact-bar__email">hello@trelmixo.com</span>
        <span class="contact-bar__phone">+71 4837160295</span>
      </div>
    </div>

    <div class="title-frame"></div>
    <h1 class="brand-title">Professional<br>Domainer</h1>

    <div class="person">
      <p class="person__name">Marisol Kettner</p>
      <p class="person__degree">B.Tech Computer Science</p>
    </div>
  </div>
</body>
</html>
```